Brindova Electrical Solutions needs a website

We need a new website designed because our current one is outdated. I would like a one-page website. We are a B2B company and want to maintain a professional appearance to appeal to project managers and directors.

for some reference, these are a few of my competitor's websites; we offer the same services.

https://valtrawire.com.au/services
https://www.drumwell.com.au/mechanical-electrical-services/
https://www.qulan.com.au/

Industry/Entity Type

Electrical

Number of Pages Required

1 page

Font styles to use
Sans Serif

Colors
0054AA
0677BA
7BADD7
CADEEF
E8F1F8

```html
<!DOCTYPE html>
<html lang="en">
<head>
<meta charset="utf-8">
<title>Brindova Electrical Solutions</title>
<link rel="stylesheet" href="https://fonts.googleapis.com/css2?family=Audiowide&family=Lato:wght@400;700;900&display=swap">
<style>
:root{
  --blue:#0054AA;--blue-mid:#0677BA;--sky:#1590D8;--light:#7BADD7;--pale:#CADEEF;--mist:#E8F1F8;
  --ink:#111;--grey:#555;--dark:#1c1c1c;--white:#fff;
}
*{box-sizing:border-box;margin:0;padding:0}
html,body{width:1200px;height:4228px;overflow:hidden}
body{position:relative;font-family:"Lato",sans-serif;color:var(--ink);background:var(--white)}
.abs{position:absolute}
.display{font-family:"Audiowide",sans-serif;letter-spacing:3px}
.accent{color:var(--sky)}
/* top bar */
.topbar{left:0;top:0;width:1200px;height:76px;background:var(--white);border-top:3px solid var(--blue)}
.brand{left:110px;top:14px;display:flex;align-items:center;gap:10px}
.brand-dot{width:46px;height:46px;border-radius:50%;background:var(--blue)}
.brand-name{font-family:"Lato",sans-serif;font-weight:900;font-size:24px;color:var(--blue-mid);letter-spacing:1px;line-height:1}
.brand-sub{font-size:10px;color:var(--blue-mid);letter-spacing:2px;font-weight:900}
.contact{top:22px;display:flex;align-items:center;gap:12px;font-size:14px;letter-spacing:1px;color:#333}
.icon{width:28px;height:28px;border-radius:50%;background:var(--sky);display:flex;align-items:center;justify-content:center}
/* nav */
.nav{left:0;top:76px;width:1200px;height:50px;background:linear-gradient(90deg,var(--blue),var(--sky))}
.nav ul{position:absolute;left:112px;top:12px;list-style:none;display:flex;gap:36px;font-size:13px;letter-spacing:1px;color:var(--white)}
.nav li.active{border:2px solid var(--white);padding:3px 8px;margin-top:-5px;font-weight:900}
.nav-cta{right:112px;top:0;width:165px;height:50px;background:#7a8a93;color:var(--white);font-size:17px;letter-spacing:1px;display:flex;align-items:center;justify-content:center;clip-path:polygon(20% 0,100% 0,100% 100%,0 100%)}
/* hero */
.hero{left:0;top:126px;width:1200px;height:521px;background:linear-gradient(180deg,#5f8fb8 0%,#7fa6c5 35%,#3d5a70 55%,#31485a 75%,#5b7891 100%)}
.hero h1{position:absolute;left:0;width:1200px;top:72px;text-align:center;font-family:"Audiowide",sans-serif;font-weight:400;font-size:54px;line-height:62px;letter-spacing:5px;color:var(--white)}
.hero-list{left:0;width:1200px;top:284px;display:flex;justify-content:center;gap:34px;color:var(--white);font-size:23px;letter-spacing:2px}
.hero-list span{display:flex;align-items:center;gap:14px}
.btn{display:flex;align-items:center;padding-left:20px;color:var(--white);background:var(--blue-mid);font-size:17px;font-weight:700;letter-spacing:1.5px;clip-path:polygon(0 0,80% 0,100% 100%,0 100%)}
/* about */
.about-img{left:122px;top:730px;width:356px;height:356px;border-radius:50%;background:linear-gradient(135deg,#c9794a,#2a5f98 65%)}
.about h2{font-size:46px;font-weight:400}
.about p{font-size:13px;line-height:28.5px;letter-spacing:1px;color:var(--grey)}
/* offer */
.offer{left:0;top:1130px;width:764px;height:746px;background:linear-gradient(135deg,var(--blue),#1560b5)}
.offer h2{position:absolute;left:111px;top:62px;font-size:40px;font-weight:400;color:var(--white)}
.offer p{position:absolute;left:111px;top:125px;width:450px;font-size:13px;font-weight:700;line-height:27.5px;letter-spacing:.8px;color:var(--white)}
.card{background:linear-gradient(160deg,#6d8aa5,#34465a 70%,#1b2430);color:var(--white);font-size:17px;font-weight:700;letter-spacing:1.5px;display:flex;align-items:flex-end;padding:0 18px 14px}
.card.framed{border:5px solid var(--white)}
/* services */
.section-title{left:0;width:1200px;text-align:center;font-size:46px;font-weight:400}
.circle{width:294px;height:294px;border-radius:50%}
.svc-label{font-size:19px;letter-spacing:1.5px;text-align:center;width:460px}
/* testimonials */
.testi{left:347px;top:2500px;width:853px;height:497px;background:var(--blue)}
.testi h2{position:absolute;left:130px;top:50px;font-size:42px;font-weight:400;color:var(--white)}
.tcard{top:2643px;width:472px;height:258px;background:var(--white);border-radius:4px;box-shadow:0 2px 12px rgba(0,0,0,.18);padding:22px 24px 0 28px}
.tail{width:0;height:0;border-top:42px solid var(--white);border-left:62px solid transparent}
.avatar{width:66px;height:66px;border-radius:50%;background:linear-gradient(#8c6a52,#3a2b22)}
.tname{font-size:15px;color:#222}
.stars{color:#f4b400;font-size:13px;letter-spacing:1px}
.tbody{font-size:12.5px;line-height:22px;color:#666;margin-top:22px}
.tmore{font-size:12px;color:#555;text-decoration:underline;margin-top:14px;display:block}
.quote{position:absolute;right:26px;top:30px;font-size:58px;line-height:40px;color:#bbb;font-family:Georgia,serif}
.arrow{width:26px;height:26px;border-radius:50%;display:flex;align-items:center;justify-content:center}
/* projects */
.project-img{left:108px;top:3162px;width:977px;height:483px;background:linear-gradient(90deg,#8c8680,#b5afa8 30%,#706860 50%,#b5afa8 70%,#8c8680)}
.dots{left:0;width:1200px;top:3681px;display:flex;justify-content:center;gap:6px}
.dots i{width:16px;height:16px;border-radius:50%;background:var(--pale)}
.dots i.on{background:var(--blue-mid)}
/* footer */
.footer{left:0;top:3810px;width:1200px;height:418px;background:var(--dark);color:var(--white)}
.footer h4{font-family:"Audiowide",sans-serif;font-weight:400;font-size:15px;letter-spacing:1.5px}
.footer ul{list-style:none;font-size:13.5px;letter-spacing:1px;line-height:29px;margin-top:20px}
.finput{left:110px;top:165px;width:318px;height:42px;background:var(--white);color:#666;font-size:13px;padding:13px 20px}
.social{width:22px;height:22px;border-radius:50%;background:var(--white)}
.copy{left:0;width:1200px;top:386px;text-align:center;font-size:13px;color:#ddd}
.rule{left:108px;top:361px;width:977px;height:1px;background:#666}
</style>
</head>
<body>

<header class="abs topbar">
  <div class="abs brand">
    <div class="brand-dot"></div>
    <div><div class="brand-name">BRINDOVA</div><div class="brand-sub">ELECTRICAL SOLUTIONS</div></div>
  </div>
  <div class="abs contact" style="left:450px">
    <span class="icon"><svg width="14" height="16" viewBox="0 0 14 16"><path d="M7 0a6 6 0 0 0-6 6c0 4.5 6 10 6 10s6-5.5 6-10a6 6 0 0 0-6-6zm0 8.5A2.5 2.5 0 1 1 7 3.5a2.5 2.5 0 0 1 0 5z" fill="#fff"/></svg></span>Sydney NSW, Australia
  </div>
  <div class="abs contact" style="left:700px">
    <span class="icon"><svg width="14" height="14" viewBox="0 0 14 14"><path d="M3 0l2.5 3-1.5 2a8 8 0 0 0 5 5l2-1.5 3 2.5-1.5 2.5C7 14 0 7 .5 1.5z" fill="#fff"/></svg></span>02 8015 4720
  </div>
  <div class="abs contact" style="left:884px">
    <span class="icon"><svg width="14" height="11" viewBox="0 0 14 11"><rect width="14" height="11" rx="1" fill="#fff"/><path d="M0 1l7 5 7-5" stroke="#1590D8" fill="none" stroke-width="1.5"/></svg></span>info@brindovasolutions.com.au
  </div>
</header>

<nav class="abs nav">
  <ul><li class="active">Home</li><li>About Us</li><li>Services</li><li>Testimonials</li><li>Projects</li></ul>
  <div class="abs nav-cta">Contact Us</div>
</nav>

<section class="abs hero" role="img" aria-label="Sydney harbour skyline with opera house reflected in the water">
  <h1>TRANSFORMING<br>PROJECTS WITH PRECISION<br>AND EXPERTISE</h1>
  <div class="abs hero-list">
    <span><svg width="22" height="22" viewBox="0 0 22 22"><circle cx="11" cy="11" r="11" fill="#fff"/><path d="M6 11h9M11 6l5 5-5 5" stroke="#333" stroke-width="2.4" fill="none"/></svg>Mechanical</span>
    <span><svg width="22" height="22" viewBox="0 0 22 22"><circle cx="11" cy="11" r="11" fill="#fff"/><path d="M6 11h9M11 6l5 5-5 5" stroke="#333" stroke-width="2.4" fill="none"/></svg>Electrical</span>
    <span><svg width="22" height="22" viewBox="0 0 22 22"><circle cx="11" cy="11" r="11" fill="#fff"/><path d="M6 11h9M11 6l5 5-5 5" stroke="#333" stroke-width="2.4" fill="none"/></svg>HVAC</span>
  </div>
  <div class="abs btn" style="left:516px;top:344px;width:168px;height:48px">Get Started</div>
</section>

<section class="about">
  <div class="abs about-img" role="img" aria-label="Technician working on a wiring panel"></div>
  <h2 class="abs display" style="left:642px;top:720px">ABOUT <span class="accent">US</span></h2>
  <p class="abs" style="left:642px;top:785px;width:455px">At brindova solution, we specialize in delivering tailored solutions that help businesses streamline their projects, improve efficiency, and ensure on-time, on-budget results. With years of experience working alongside project managers and directors, we understand the complexities of large-scale initiatives and the need for reliable, strategic support.</p>
  <div class="abs btn" style="left:644px;top:977px;width:162px;height:49px">Read More</div>
</section>

<section class="abs offer">
  <h2 class="display">WHAT WE OFFER</h2>
  <p>We offer comprehensive services designed to support and optimize every phase of your project, from inception to completion. We focus on providing practical, results-driven solutions that help you meet deadlines, stay within budget, and exceed project objectives.</p>
</section>
<div class="abs card framed" style="left:591px;top:1198px;width:246px;height:202px" role="img" aria-label="Technician checking a mechanical gas valve">Mechanical Electrical</div>
<div class="abs card" style="left:853px;top:1203px;width:241px;height:192px" role="img" aria-label="Technician servicing an HVAC control cabinet">BMCS &amp; HVAC</div>
<div class="abs card" style="left:110px;top:1420px;width:237px;height:190px" role="img" aria-label="Electrical design drawing on a monitor">Project Design</div>
<div class="abs card" style="left:358px;top:1420px;width:242px;height:190px" role="img" aria-label="Engineer in a switch room">Engineering</div>
<div class="abs card" style="left:611px;top:1420px;width:237px;height:190px" role="img" aria-label="Team reviewing project plans">Project Management</div>
<div class="abs card" style="left:861px;top:1420px;width:233px;height:190px" role="img" aria-label="Technician commissioning a control panel">Commissioning</div>
<div class="abs card" style="left:110px;top:1625px;width:240px;height:190px;line-height:27px" role="img" aria-label="Workers in a commercial fit-out">Commercial &amp;<br>Industrial Projects</div>
<div class="abs card" style="left:362px;top:1625px;width:240px;height:190px;line-height:27px" role="img" aria-label="Installed switchboard">Switchboard Design &amp;<br>Installation</div>

<h2 class="abs display section-title" style="top:1953px">OUR <span class="accent">SERVICES</span></h2>
<div class="abs circle" style="left:217px;top:2074px;background:radial-gradient(circle,#aaa,#6f6a66)" role="img" aria-label="Mechanical electrical control panels on a wall"></div>
<div class="abs circle" style="left:698px;top:2074px;background:radial-gradient(circle,#d8d4c6,#4b5560);box-shadow:0 8px 24px rgba(0,0,0,.25)" role="img" aria-label="Building management control cabinet"></div>
<svg class="abs" style="left:806px;top:2312px" width="72" height="72"><circle cx="36" cy="36" r="36" fill="#fff"/><circle cx="36" cy="36" r="27" fill="#0677BA"/><circle cx="36" cy="36" r="11" stroke="#fff" stroke-width="3" fill="none"/></svg>
<div class="abs svc-label" style="left:132px;top:2390px">Mechanical Electrical Services</div>
<div class="abs svc-label accent" style="left:615px;top:2392px">Building Management Control Systems</div>

<section class="abs testi"><h2 class="display">CLIENT TESTIMONIALS</h2></section>
<div class="abs arrow" style="left:42px;top:2773px;background:#ccc"><svg width="14" height="14"><path d="M12 7H3M7 3L3 7l4 4" stroke="#fff" stroke-width="2" fill="none"/></svg></div>
<div class="abs arrow" style="left:1122px;top:2773px;background:#fff"><svg width="14" height="14"><path d="M2 7h9M7 3l4 4-4 4" stroke="#0054AA" stroke-width="2" fill="none"/></svg></div>

<article class="abs tcard" style="left:113px">
  <div style="display:flex;gap:14px;margin-left:-10px"><div class="avatar" role="img" aria-label="Client portrait"></div>
    <div style="padding-top:10px"><div class="tname">Lorna Vey, Client</div><div class="stars"><span style="display:inline-block;width:11px;height:11px;border-radius:50%;background:#999;vertical-align:-1px"></span> ★★★★★</div></div></div>
  <span class="quote">”</span>
  <p class="tbody" style="margin-top:18px">Duis aute irure dolor in reprehenderit in voluptate velit esse cillum dolore eu fugiat nulla pariatur. Excepteur sint occaecat cupidatat non proident, sunt in culpa qui officia deserunt mollit anim id est laborum. Sed ut perspiciatis unde omnis iste natus error sit voluptatem accusantium doloremque laudantium.</p>
  <span class="tmore">Read More....</span>
</article>
<div class="abs tail" style="left:388px;top:2900px"></div>

<article class="abs tcard" style="left:615px">
  <div style="display:flex;gap:14px;margin-left:-10px"><div class="avatar" role="img" aria-label="Client portrait"></div>
    <div style="padding-top:10px"><div class="tname">Tasha Merrin</div><div class="stars"><span style="display:inline-block;width:11px;height:11px;border-radius:50%;background:#999;vertical-align:-1px"></span> ★★★★★</div></div></div>
  <span class="quote">”</span>
  <p class="tbody" style="margin-top:18px">Lorem ipsum dolor sit amet, consectetur adipiscing elit, sed do eiusmod tempor incididunt ut labore et dolore magna aliqua. Ut enim ad minim veniam, quis nostrud exercitation ullamco laboris nisi ut aliquip ex ea commodo consequat.</p>
  <span class="tmore" style="margin-top:36px">Read More....</span>
</article>
<div class="abs tail" style="left:888px;top:2900px"></div>

<h2 class="abs display section-title" style="top:3073px">LATEST <span class="accent">PROJECTS</span></h2>
<div class="abs project-img" role="img" aria-label="Two variable speed drives mounted either side of a cable tray"></div>
<div class="abs dots"><i></i><i></i><i class="on"></i><i></i><i></i></div>

<footer class="abs footer">
  <div class="abs brand" style="left:110px;top:78px">
    <div class="brand-dot" style="width:60px;height:60px;background:#fff"></div>
    <div><div class="brand-name" style="color:#fff;font-size:30px">BRINDOVA</div><div class="brand-sub" style="color:#fff;font-size:11px">ELECTRICAL SOLUTIONS</div></div>
  </div>
  <div class="abs finput">Enter Email Address</div>
  <div class="abs btn" style="left:110px;top:217px;width:170px;height:48px;background:var(--sky)">Subscribe</div>
  <div class="abs" style="left:117px;top:286px;display:flex;gap:7px"><i class="social" style="background:var(--sky)"></i><i class="social"></i><i class="social"></i></div>

  <div class="abs" style="left:480px;top:92px"><h4>QUICK LINKS</h4><ul style="margin-left:6px"><li>Home</li><li>About Us</li><li>Services</li><li>Testimonials</li><li>Projects</li><li>Contact Us</li></ul></div>
  <div class="abs" style="left:674px;top:92px"><h4>HELP LINKS</h4><ul><li>Privacy Policy</li><li>Terms &amp; Conditions</li><li>Disclaimer</li><li>FAQ's</li><li>Support</li></ul></div>
  <div class="abs" style="left:884px;top:92px"><h4>CONTACT INFO</h4>
    <ul style="line-height:52px;margin-top:4px">
      <li style="display:flex;align-items:center;gap:14px"><span class="icon" style="background:#fff;width:24px;height:24px"><svg width="12" height="14" viewBox="0 0 14 16"><path d="M7 0a6 6 0 0 0-6 6c0 4.5 6 10 6 10s6-5.5 6-10a6 6 0 0 0-6-6z" fill="#1c1c1c"/></svg></span>Sydney NSW, Australia</li>
      <li style="display:flex;align-items:center;gap:14px"><span class="icon" style="background:#fff;width:24px;height:24px"><svg width="12" height="12" viewBox="0 0 14 14"><path d="M3 0l2.5 3-1.5 2a8 8 0 0 0 5 5l2-1.5 3 2.5-1.5 2.5C7 14 0 7 .5 1.5z" fill="#1c1c1c"/></svg></span>02 8015 4720</li>
      <li style="display:flex;align-items:center;gap:14px"><span class="icon" style="background:#fff;width:24px;height:24px"><svg width="12" height="9" viewBox="0 0 14 11"><rect width="14" height="11" fill="#1c1c1c"/><path d="M0 1l7 5 7-5" stroke="#fff" fill="none"/></svg></span>info@brindovasolutions.com.au</li>
    </ul></div>
  <div class="abs rule"></div>
  <div class="abs copy">© Copyright 2024 Brindova Electrical Solutions | All Rights Reserved</div>
</footer>

</body>
</html>
```